Lumen Harbor Sales Aid and Contract

I started my own company and the company I worked for has a sales aid / contract that I want to replicate. I want it to be simpler similar design in an editable PDF Form. It needs to be different and better in my company colors see logo attached I need to be able to edit the fine print and will need the KP Inc. changed to Lumen Harbor through out the agreement. Follow same flow but instead of Platinum Gold and Silver I would like Gold Silver and Bronze with different badges

```html
<!DOCTYPE html>
<html lang="en">
<head>
<meta charset="utf-8">
<title>Lumen Harbor Agreement</title>
<link href="https://fonts.googleapis.com/css2?family=Arimo:ital,wght@0,400;0,700;1,400&family=Montserrat:wght@500&display=swap" rel="stylesheet">
<style>
  :root {
    --ink: #3a3a3a;
    --ink-dark: #111111;
    --band: #000000;
    --paper: #ffffff;
    --brand-grey: #8a8a8a;
    --rule: #222222;
  }
  html, body { margin: 0; padding: 0; overflow: hidden; }
  body { width: 879px; height: 1200px; background: var(--paper); }
  .sheet {
    position: relative; width: 879px; height: 1200px; overflow: hidden;
    font-family: "Arimo", Arial, sans-serif; color: var(--ink);
  }
  .header-band {
    position: absolute; left: 0; top: 0; width: 879px; height: 112px; background: var(--band);
  }
  .doc-title {
    position: absolute; left: 55px; top: 32px; margin: 0;
    font-family: "Montserrat", Arial, sans-serif; font-weight: 500;
    font-size: 44px; line-height: 1; color: var(--paper); letter-spacing: 0.5px;
  }
  .brand-name {
    position: absolute; left: 640px; top: 52px;
    font-family: "Arimo", Arial, sans-serif; font-size: 11px; letter-spacing: 2.5px;
    color: var(--brand-grey);
  }
  .brand-mark { position: absolute; left: 779px; top: 39px; }
  .block { position: absolute; left: 56px; width: 772px; font-size: 13.6px; line-height: 16.4px; margin: 0; }
  .block b { color: #2b2b2b; }
  .block .dark { color: var(--ink-dark); }
  .terms { top: 155px; }
  .lien { top: 282px; }
  .form-row {
    position: absolute; left: 56px; width: 771px; display: flex; align-items: flex-end;
    font-size: 13.6px; line-height: 16px; white-space: nowrap;
  }
  .line { border-bottom: 1.3px solid var(--rule); height: 12px; margin-right: 4px; }
  .grow { flex: 1; }
  .special { position: absolute; left: 56px; top: 554px; font-size: 13.6px; }
  .sign-row { top: 670px; width: 745px; }
  .sign-row .company { font-size: 12.4px; }
  .clauses { position: absolute; left: 56px; width: 772px; top: 719px; font-size: 12.1px; line-height: 14.6px; color: #222; }
  .clause { margin: 0 0 14.6px 0; }
  .clause b { color: #111; }
  .clause .co { color: #555; }
</style>
</head>
<body>
<div class="sheet">
  <header class="header-band">
    <h1 class="doc-title">Agreement</h1>
    <div class="brand-name">LUMEN HARBOR</div>
    <svg class="brand-mark" width="44" height="44" viewBox="0 0 44 44" aria-hidden="true">
      <circle cx="22" cy="22" r="21" fill="#ffffff"/>
    </svg>
  </header>

  <p class="block terms"><b>Terms:</b> Your guarantee (<i>based on your choice</i>) is on workmanship and not materials, which would be covered under the manufacturer’s warranty. This workmanship guarantee is non transferable.<br>
  <b>Qualification:</b> Your investment of the&nbsp; Gold / Silver / Bronze system must be paid in full. During the terms of the workmanship guarantee, if defects in workmanship are found, original home owner must notify Lumen Harbor within 10 days by telephone or e-mail and confirm by written notice.<br>
  <b>Limitations:</b> Guarantee does not cover acts of omissions of other trades, natural weathering, recommended maintenance, <span class="dark">lightning, flood, earthquake or any natural disaster</span> or unusual phenomenon of elements.</p>

  <p class="block lien"><b>PRE-LIEN NOTICE</b> to (Owners Authorized Agents) by Contractor:<br>
  *Any person or company supplying labor or materials for this improvement to your property may file a lien against your property if that person or company is not paid for contributions.<br>
  <b>Authorization:</b> I have authorized work task to be completed. I agree that seller retains title to equipment or product and materials furnished until final payment is satisfied.</p>

  <div class="form-row" style="top:406px">Date:&nbsp;<span class="line" style="width:82px"></span>Level plan :&nbsp;<span class="line" style="width:98px"></span>Start date:&nbsp;<span class="line" style="width:106px"></span>Planned completion date:&nbsp;<span class="line grow" style="margin-right:0"></span></div>
  <div class="form-row" style="top:428px">Client’s Name:&nbsp;<span class="line" style="width:278px"></span><span class="line grow" style="margin-right:0"></span></div>
  <div class="form-row" style="top:450px">Project Location address:&nbsp;<span class="line grow" style="margin-right:0"></span></div>
  <div class="form-row" style="top:472px">Total Investment:&nbsp;<span class="line" style="width:254px;margin-right:0"></span>Payment terms:<span class="line grow" style="margin-right:0"></span></div>
  <div class="form-row" style="top:494px">Amount down:&nbsp;<span class="line" style="width:279px;margin-right:0"></span>Payment method:&nbsp;<span class="line" style="width:156px;margin-right:0"></span>Date:<span class="line grow" style="margin-right:0"></span></div>
  <div class="form-row" style="top:516px">Clients authorization:&nbsp;<span class="line" style="width:320px"></span>Printed name<span class="line grow" style="margin-right:0"></span></div>

  <div class="special">Special instructions:</div>

  <div class="form-row sign-row"><span class="company">Lumen Harbor</span>&nbsp;: By<span class="line" style="width:237px"></span>Title<span class="line" style="width:196px;margin-right:0"></span>Date:<span class="line grow" style="margin-right:0"></span></div>

  <div class="clauses">
    <p class="clause"><b>1. Investment</b>: Client shall pay the amount of agreement for completion of work. If there is a change at the time of sale in the applicable sales tax, the Investment will be adjusted accordingly.</p>
    <p class="clause"><b>2. Investment amount</b>: A 33% down deposit on agreed investment is required at time of an authorized agreement for amounts over 10,000 and 50% down for investments under $10,000. Remainder of balance is due at time of delivery/installation or bill progress. Interest will be charged at 18% APR on payments that are thirty (30) days past due.</p>
    <p class="clause"><b>3.Additional Options:</b> The Client may request changes (Additional Options) from the original plans. All Additional Options must be in writing and authorized by both parties. The Client must authorize or approve Additional Options and before Lumen Harbor. will proceed with the additional scope of work. 100% of additional amount due upon approval except if additional option is over $30,000, 50% due upon approval.</p>
    <p class="clause"><b>4. Hidden, Concealed and Unforeseeable Conditions:</b> The parties agree that in the event a condition arises that requires an extra cost, they shall proceed as follows: <span class="co">Lumen Harbor</span> shall notify Client verbally at once to expedite agreement as to the charge to correct or cure such condition, and provide a written estimate as soon as practicable. All parties must agree to such extra amount, or agree to a resolution method, or this Agreement may be canceled by either party. For purposes of this section, a “hidden, concealed and unforeseeable condition” shall mean a condition not apparent to <span class="co">Lumen Harbor</span>. This could include but is not limited to a sudden unavailability or scarcity of materials needed to complete project, unexpected surge in costs for materials, or structural problems in original structure that prohibit a secure installation.</p>
    <p class="clause"><b>5. Building Codes</b>: <span class="co">Lumen Harbor</span> is agreeing to perform a specific scope of work designed or ordered by the Client or Client’s architect for a specific investment. If that specific scope of work needs to be changed in order to meet applicable building codes, then the Client may authorize, at the <i>Client’s</i> added expense, additional work in order to satisfy the building codes and inspectors. The code work will be done in accordance with the Additional Options clause (#2 above).</p>
    <p class="clause"><b>6. Cancellation of Agreement</b>: If Agreement is canceled by Client prior to start of Agreement work scope, <span class="co">Lumen Harbor</span> reserves the right to charge an administration fee of 5% or $5,000, whichever is less.</p>
  </div>
</div>
</body>
</html>
```